Mesh Banner Design for Business Premises

We require the design of a large mesh banner to be installed across the front fence of our warehouse. The banner should prominently feature our existing Trelborn logo and brand colours (yellow, white, and black) and be designed to be highly visible from the road.

The overall aesthetic should be strong, masculine, and industrial, reflecting the nature of the scaffolding and construction industry. The background should be predominantly black, with our branding incorporated in yellow and white for strong contrast and readability.

The banner should clearly communicate the full scope of services we provide, including:

Scaffold Design
Scaffold Engineering
Scaffold Installation / Erection
Scaffold Dismantling

It should also indicate the types of projects and clients we service, including:

Commercial
Industrial
Residential
Civil

The design should feel bold and professional, with a construction-oriented style that aligns with the scaffolding industry. It should be clean, impactful, and easy to read from a distance, ensuring passing traffic can quickly understand our services.

Where possible, subtle industrial or structural design elements (such as scaffold components, steel textures, or linework) may be incorporated into the background to reinforce the industry theme while keeping the layout uncluttered.

The final design will be produced as a large-format mesh banner for outdoor installation, so it should be created with this application and viewing distance in mind.

```html
<!DOCTYPE html>
<html lang="en">
<head>
<meta charset="utf-8">
<title>Trelborn Scaffold Services Banner</title>
<link rel="stylesheet" href="https://fonts.googleapis.com/css2?family=Orbitron:wght@700;800&display=swap">
<style>
  :root {
    --stage: #d8d8d8;
    --black: #070707;
    --charcoal: #262626;
    --gold: #e6a826;
    --white: #f4f4f4;
  }
  html, body {
    margin: 0;
    width: 1200px;
    height: 864px;
    overflow: hidden;
    background: var(--stage);
  }
  .banner {
    position: absolute;
    left: 0;
    top: 132px;
    width: 1200px;
    height: 600px;
    background: radial-gradient(ellipse 75% 90% at 25% 45%, var(--charcoal) 0%, #141414 45%, var(--black) 80%);
    font-family: "Orbitron", sans-serif;
    font-weight: 700;
    color: var(--white);
    overflow: hidden;
  }
  .hazard-band {
    position: absolute;
    left: 0;
    width: 1200px;
    height: 68px;
    display: block;
  }
  .hazard-band--top { top: 0; }
  .hazard-band--bottom { bottom: 0; }

  .brand-mark {
    position: absolute;
    left: 244px;
    top: 144px;
    width: 130px;
    height: 130px;
    border-radius: 50%;
    background: var(--gold);
  }
  .brand-name {
    position: absolute;
    left: 82px;
    top: 329px;
    margin: 0;
    font-size: 36px;
    font-weight: 800;
    letter-spacing: 0.62em;
    line-height: 1;
    color: var(--white);
    white-space: nowrap;
  }
  .services {
    position: absolute;
    left: 606px;
    top: 212px;
  }
  .services__title {
    margin: 0 0 17px;
    font-size: 26px;
    font-weight: 800;
    letter-spacing: 0.2em;
    line-height: 32px;
    color: var(--gold);
    white-space: nowrap;
  }
  .services__list {
    list-style: none;
    margin: 0;
    padding: 0;
  }
  .services__list li {
    font-size: 22px;
    letter-spacing: 0.2em;
    line-height: 35px;
    white-space: nowrap;
  }
  .sectors {
    position: absolute;
    left: 80px;
    width: 1040px;
    top: 423px;
    height: 32px;
    display: flex;
    justify-content: space-between;
    align-items: center;
    font-size: 21px;
    letter-spacing: 0.2em;
    white-space: nowrap;
  }
  .sectors__divider {
    display: block;
    width: 5px;
    height: 32px;
    background: var(--white);
  }
</style>
</head>
<body>
  <main class="banner">
    <svg class="hazard-band hazard-band--top" viewBox="0 0 1200 68" aria-hidden="true">
      <defs>
        <pattern id="hazard-stripes" width="68" height="68" patternUnits="userSpaceOnUse" patternTransform="skewX(-39)">
          <rect width="68" height="68" fill="var(--black)"/>
          <rect x="17" width="34" height="68" fill="var(--gold)"/>
        </pattern>
      </defs>
      <rect width="1200" height="68" fill="url(#hazard-stripes)"/>
    </svg>

    <span class="brand-mark" aria-hidden="true"></span>
    <h1 class="brand-name">TRELBORN</h1>

    <section class="services">
      <h2 class="services__title">SCAFFOLD SERVICES</h2>
      <ul class="services__list">
        <li>DESIGN · ENGINEERING</li>
        <li>INSTALLATION/ERECTION</li>
        <li>DISMANTLING</li>
      </ul>
    </section>

    <div class="sectors">
      <span>COMMERCIAL</span>
      <span class="sectors__divider"></span>
      <span>INDUSTRIAL</span>
      <span class="sectors__divider"></span>
      <span>RESIDENTIAL</span>
      <span class="sectors__divider"></span>
      <span>CIVIL</span>
    </div>

    <svg class="hazard-band hazard-band--bottom" viewBox="0 0 1200 68" aria-hidden="true">
      <rect width="1200" height="68" fill="url(#hazard-stripes)"/>
    </svg>
  </main>
</body>
</html>
```